KT Crewing business card

Require business card which includes:
Company name: KT CREWING PTY LTD
Email: Mick@ktcrewing.com.au
Phone: 0431 556 208
ACN: 517 238 649

slogan: Onsite Auto Electrician Labour hire

Details and logo on top side
Logo only on bottom side

colour codes : #F15A29 , #939598

Target Market(s)

Western Australia mining sector

Industry/Entity Type

Mining

Contact Information for Business Card

Require business card which includes: Company name: KT CREWING PTY LTD Email: Mick@ktcrewing.com.au Phone: 0431 556 208 ACN: 517 238 649 slogan: Onsite Auto Electrician Labour hire Details and logo on top side Logo only on bottom side colour codes : #F15A29 , #939598

Colors
EE7325
F08F49
F5BC92
FAE3D3
FDF4ED

Requirements
Must have
• double sided

```html
<!DOCTYPE html>
<html lang="en">
<head>
<meta charset="utf-8">
<title>KT Crewing Business Card</title>
<link rel="stylesheet" href="https://fonts.googleapis.com/css2?family=Oswald:wght@400;500;600&family=Open+Sans:wght@400&display=swap">
<style>
  :root {
    --card-grey: #4a4a4b;
    --brand-orange: #f15a29;
    --band-orange: #ee7325;
    --brand-silver: #939598;
    --text-light: #ececec;
    --ghost-mark: #564843;
    --page: #ffffff;
    --label: #111111;
  }
  * { box-sizing: border-box; margin: 0; padding: 0; }
  html, body { width: 1200px; height: 437px; overflow: hidden; background: var(--page); }
  .canvas { position: relative; width: 1200px; height: 437px; }

  .card {
    position: absolute;
    top: 15px;
    width: 556px;
    height: 318px;
    background: var(--card-grey);
    box-shadow: 2px 3px 6px rgba(0,0,0,0.35);
    overflow: hidden;
  }
  .card--front { left: 19px; }
  .card--back { left: 630px; }
  .card__art { position: absolute; inset: 0; width: 556px; height: 318px; }

  .brand-name {
    font-family: "Oswald", sans-serif;
    font-weight: 600;
    color: var(--brand-orange);
    line-height: 1;
    white-space: nowrap;
  }
  .front-brand {
    position: absolute;
    left: 0; right: 0;
    top: 118px;
    text-align: center;
    font-size: 58px;
  }
  .front-slogan {
    position: absolute;
    left: 0; right: 0;
    top: 206px;
    text-align: center;
    font-family: "Oswald", sans-serif;
    font-weight: 500;
    font-size: 10px;
    letter-spacing: 0.3px;
    color: var(--brand-silver);
    text-transform: uppercase;
  }

  .back-ghost {
    position: absolute;
    left: 0; right: 0;
    top: 92px;
    text-align: center;
    font-family: "Oswald", sans-serif;
    font-weight: 600;
    font-size: 92px;
    line-height: 1;
    color: var(--ghost-mark);
    white-space: nowrap;
  }
  .company-title {
    position: absolute;
    left: 0; right: 0;
    top: 16px;
    text-align: center;
    font-family: "Oswald", sans-serif;
    font-weight: 500;
    font-size: 22px;
    letter-spacing: 1px;
    color: var(--text-light);
  }
  .contact-list {
    position: absolute;
    left: 17px;
    top: 84px;
    list-style: none;
    font-family: "Oswald", sans-serif;
    font-weight: 500;
    font-size: 14px;
    color: #ffffff;
    text-transform: uppercase;
    letter-spacing: 0.3px;
  }
  .contact-list li { height: 39px; line-height: 20px; }
  .back-brand {
    position: absolute;
    right: 16px;
    bottom: 18px;
    font-size: 28px;
  }

  .side-label {
    position: absolute;
    top: 362px;
    font-family: "Open Sans", sans-serif;
    font-weight: 400;
    font-size: 52px;
    line-height: 1;
    color: var(--label);
    text-align: center;
    width: 556px;
  }
  .side-label--front { left: 19px; }
  .side-label--back { left: 630px; }
</style>
</head>
<body>
<main class="canvas">

  <section class="card card--front" aria-label="Card front">
    <svg class="card__art" viewBox="0 0 556 318" aria-hidden="true">
      <rect x="0" y="40" width="556" height="4" fill="var(--brand-silver)" opacity="0.45"/>
      <rect x="0" y="48" width="556" height="16" fill="var(--band-orange)"/>
      <rect x="0" y="254" width="556" height="16" fill="var(--band-orange)"/>
      <rect x="0" y="274" width="556" height="4" fill="var(--brand-silver)" opacity="0.45"/>
    </svg>
    <p class="brand-name front-brand">KT Crewing</p>
    <p class="front-slogan">Onsite Auto Electrician Labour Hire</p>
  </section>

  <section class="card card--back" aria-label="Card back">
    <p class="back-ghost" aria-hidden="true">KT Crewing</p>
    <svg class="card__art" viewBox="0 0 556 318" aria-hidden="true">
      <rect x="266" y="0" width="6" height="318" fill="var(--brand-orange)"/>
    </svg>
    <h1 class="company-title">KT CREWING PTY LTD</h1>
    <ul class="contact-list">
      <li>Phone: 0431 556 208</li>
      <li>Email: Mick@ktcrewing.com.au</li>
      <li>ACN: 517 238 649</li>
    </ul>
    <p class="brand-name back-brand">KT Crewing</p>
  </section>

  <p class="side-label side-label--front">FRONT</p>
  <p class="side-label side-label--back">BACK</p>

</main>
</body>
</html>
```